A need a professional website for An IT Company

We need a very professional but clean wordpress design for our website.
We are into IT solutions, we manage serrvers, unified communications and do computer repairs and maintenance. We want a wordpress design that will promote our offering and online presense greatly. Our design should be very clean and mordern for easy navigation.
- A frontpage slider
contact form with Google map integration

```html
<!DOCTYPE html>
<html lang="en">
<head>
<meta charset="utf-8">
<title>Veranto – About</title>
<link rel="stylesheet" href="https://fonts.googleapis.com/css2?family=Arimo:ital,wght@0,400;0,700;1,400&family=Carlito:wght@400;700&family=Questrial&display=swap">
<style>
  :root {
    --brand: #6c4650;
    --brand-dark: #583640;
    --brand-light: #8a6470;
    --accent: #8fa37a;
    --ink: #1f1f1f;
    --text: #333333;
    --muted: #8c8c8c;
    --soft: #5a5a5a;
    --panel-top: #ececec;
    --panel-bottom: #d9d9d9;
    --panel-border: #c9c9c9;
    --rule: #bdbdbd;
    --white: #ffffff;
    --social: #4f7fb3;
    --badge: #d5dde6;
  }
  * { box-sizing: border-box; margin: 0; padding: 0; }
  html, body { width: 1200px; height: 800px; overflow: hidden; background: var(--white); }
  body { position: relative; font-family: "Arimo", Arial, sans-serif; color: var(--text); }
  ul { list-style: none; }

  /* Header */
  .brand { position: absolute; left: 19px; top: 44px; }
  .brand-name {
    display: flex; align-items: center; gap: 10px;
    font-family: "Arimo", Arial, sans-serif; font-weight: 400; font-size: 36px; line-height: 1;
    color: var(--brand);
  }
  .brand-mark { width: 22px; height: 22px; background: var(--brand); }
  .brand-tagline { margin: 8px 0 0 2px; font-size: 13px; color: var(--muted); }

  .follow { position: absolute; right: 22px; top: 32px; display: flex; align-items: center; gap: 6px; }
  .follow-label { font-size: 15px; color: var(--soft); margin-right: 2px; }
  .follow-icon { width: 28px; height: 28px; border-radius: 4px; background: var(--social); }

  .badge { position: absolute; left: 782px; top: 66px; width: 96px; height: 44px; border-radius: 4px; background: var(--badge); }
  .header-divider { position: absolute; left: 900px; top: 70px; width: 1px; height: 32px; background: #d0d0d0; }
  .callus { position: absolute; right: 22px; top: 74px; font-size: 19px; font-style: italic; color: var(--ink); }
  .callus-label { color: var(--brand); }

  /* Navigation */
  .main-nav {
    position: absolute; left: 19px; top: 122px; width: 1158px; height: 43px;
    background: linear-gradient(var(--brand-light), var(--brand) 30%, var(--brand-dark));
    border-radius: 4px;
  }
  .nav-list { display: flex; height: 100%; }
  .nav-item {
    display: flex; align-items: center; justify-content: center;
    font-size: 17px; color: var(--white);
  }
  .nav-item.is-active {
    position: relative; margin-top: 2px; height: 41px;
    background: linear-gradient(#ffffff, #e2e2e2); color: var(--brand);
  }
  .nav-item.is-active::before {
    content: ""; position: absolute; top: -2px; left: 50%; margin-left: -7px;
    border: 7px solid transparent; border-top-color: var(--accent); border-bottom: 0;
  }
  .search {
    position: absolute; right: 12px; top: 9px; width: 221px; height: 26px;
    background: var(--white); border-radius: 3px; display: flex; align-items: center;
  }
  .search-field { flex: 1; padding-left: 7px; font-size: 12px; color: #b5b5b5; }
  .search-button { width: 28px; height: 24px; border-left: 1px solid #dcdcdc; display: flex; align-items: center; justify-content: center; }

  /* Sidebar */
  .panel {
    position: absolute; left: 20px; width: 293px;
    background: linear-gradient(var(--panel-top), var(--panel-bottom));
    border: 1px solid var(--panel-border);
  }
  .panel-title {
    font-family: "Carlito", sans-serif; font-weight: 700; font-size: 20px;
    color: var(--ink); padding: 10px 0 0 23px;
  }
  .features { top: 190px; height: 253px; }
  .feature-list { margin: 8px 12px 0 23px; }
  .feature-link {
    font-family: "Carlito", sans-serif; font-weight: 700; font-size: 17px;
    color: var(--soft); height: 32.5px; line-height: 31px;
    border-bottom: 1px solid var(--white); box-shadow: 0 1px 0 #c8c8c8;
  }
  .feature-link:last-child { border: 0; box-shadow: none; }
  .feature-link.is-current { color: var(--brand); }

  .testimonials { top: 467px; height: 166px; }
  .testimonial-quote { padding: 14px 20px 0 24px; font-size: 16px; line-height: 26.5px; color: var(--text); }
  .testimonials::after {
    content: ""; position: absolute; left: 244px; bottom: -16px;
    border: 15px solid transparent; border-top: 16px solid var(--panel-bottom); border-bottom: 0;
  }
  .testimonial-author { position: absolute; right: 889px; top: 654px; font-size: 15px; color: var(--soft); }

  /* Content */
  .content { position: absolute; left: 331px; top: 195px; width: 847px; }
  .page-title {
    font-family: "Questrial", sans-serif; font-weight: 400; font-size: 26px;
    color: var(--brand); padding: 0 0 4px 4px;
    border-bottom: 1px solid var(--rule);
    box-shadow: 0 6px 8px -6px rgba(0,0,0,.12);
  }
  .intro { margin-top: 17px; font-size: 14.4px; line-height: 22.7px; text-align: justify; color: var(--ink); }
  .sub-heading { margin-top: 16px; font-family: "Questrial", sans-serif; font-weight: 400; font-size: 22px; color: var(--soft); }
  .point-list { margin-top: 11px; display: grid; grid-template-columns: 456px 1fr; row-gap: 18.5px; }
  .point { display: flex; align-items: center; gap: 10px; font-size: 15px; font-weight: 700; color: var(--muted); }

  /* Footer */
  .site-footer {
    position: absolute; left: 19px; top: 716px; width: 1158px; height: 44px;
    background: linear-gradient(#f2f2f2, #d8d8d8);
    font-size: 14px; color: #9a9a9a; padding: 14px 0 0 19px;
  }
</style>
</head>
<body>
  <header class="site-header">
    <div class="brand">
      <div class="brand-name"><span class="brand-mark"></span><span>Veranto</span></div>
      <div class="brand-tagline">...dependable IT services</div>
    </div>

    <div class="follow">
      <span class="follow-label">Follow us:</span>
      <span class="follow-icon" role="img" aria-label="Professional network profile"></span>
      <span class="follow-icon" role="img" aria-label="Social network page"></span>
      <span class="follow-icon" role="img" aria-label="Microblog profile"></span>
    </div>

    <div class="badge" role="img" aria-label="Certified partner badge"></div>
    <div class="header-divider"></div>
    <p class="callus"><span class="callus-label">Call us :</span> +(000) 555-013-2048</p>

    <nav class="main-nav">
      <ul class="nav-list">
        <li class="nav-item" style="width:115px">Home</li>
        <li class="nav-item is-active" style="width:101px">About</li>
        <li class="nav-item" style="width:102px">Services</li>
        <li class="nav-item" style="width:126px">Clients</li>
        <li class="nav-item" style="width:60px">Blog</li>
        <li class="nav-item" style="width:162px">Contact Us</li>
        <li class="nav-item" style="width:82px">Sitemap</li>
      </ul>
      <div class="search">
        <span class="search-field">Search</span>
        <span class="search-button">
          <svg width="16" height="16" viewBox="0 0 16 16" aria-hidden="true">
            <circle cx="6.5" cy="6.5" r="4.8" fill="none" stroke="#333" stroke-width="2"/>
            <line x1="10" y1="10" x2="14.5" y2="14.5" stroke="#333" stroke-width="2.2" stroke-linecap="round"/>
          </svg>
        </span>
      </div>
    </nav>
  </header>

  <aside class="sidebar">
    <section class="panel features">
      <h2 class="panel-title">FEATURES</h2>
      <ul class="feature-list">
        <li class="feature-link">Our MIssion</li>
        <li class="feature-link is-current">Employment</li>
        <li class="feature-link">Solutions you need</li>
        <li class="feature-link">Why Choose Us</li>
        <li class="feature-link">Partenship</li>
        <li class="feature-link">Prfession Research</li>
      </ul>
    </section>

    <section class="panel testimonials">
      <h2 class="panel-title">TESTIMONIALS</h2>
      <p class="testimonial-quote">Lorem ipsum dolor sit amet, con-sectetuer adipiscing elit. Lorem ipsum dolor sit amet, consectetuer adipiscing elit.</p>
    </section>
    <p class="testimonial-author">Company Director Name</p>
  </aside>

  <main class="content">
    <h1 class="page-title">About</h1>
    <p class="intro">Praesent vestibulum molestie lacus. Aenean nonummy hendrerit mauris. Phasellus porta. Fusce suscipit varius mi. Cum sociis natoque penatibus et magnis dis parturient montes, nascetur ridiculus mus. Nulla dui. Fusce feugiat malesuada odio. Morbi nunc odio, gravida at, cursus nec, luctus a, lorem. Maecenas tristique orci ac sem. Duis ultricies pharetra magna. Donec accumsan malesuada orci. Donec sit amet eros.</p>
    <h2 class="sub-heading">Sub heading</h2>
    <ul class="point-list">
      <li class="point"><svg width="10" height="13" viewBox="0 0 10 13" aria-hidden="true"><path d="M2 1.5l5 5-5 5" fill="none" stroke="#6b6b6b" stroke-width="2.6"/></svg>Praesent vestibulum molestie lacus. Aenean .</li>
      <li class="point"><svg width="10" height="13" viewBox="0 0 10 13" aria-hidden="true"><path d="M2 1.5l5 5-5 5" fill="none" stroke="#6b6b6b" stroke-width="2.6"/></svg>Praesent vestibulum molestie lacus. Aenean .</li>
      <li class="point"><svg width="10" height="13" viewBox="0 0 10 13" aria-hidden="true"><path d="M2 1.5l5 5-5 5" fill="none" stroke="#6b6b6b" stroke-width="2.6"/></svg>Praesent vestibulum molestie lacus. Aenean .</li>
      <li class="point"><svg width="10" height="13" viewBox="0 0 10 13" aria-hidden="true"><path d="M2 1.5l5 5-5 5" fill="none" stroke="#6b6b6b" stroke-width="2.6"/></svg>Praesent vestibulum molestie lacus. Aenean .</li>
      <li class="point"><svg width="10" height="13" viewBox="0 0 10 13" aria-hidden="true"><path d="M2 1.5l5 5-5 5" fill="none" stroke="#6b6b6b" stroke-width="2.6"/></svg>Praesent vestibulum molestie lacus. Aenean .</li>
      <li class="point"><svg width="10" height="13" viewBox="0 0 10 13" aria-hidden="true"><path d="M2 1.5l5 5-5 5" fill="none" stroke="#6b6b6b" stroke-width="2.6"/></svg>Praesent vestibulum molestie lacus. Aenean .</li>
      <li class="point"><svg width="10" height="13" viewBox="0 0 10 13" aria-hidden="true"><path d="M2 1.5l5 5-5 5" fill="none" stroke="#6b6b6b" stroke-width="2.6"/></svg>Praesent vestibulum molestie lacus. Aenean .</li>
      <li class="point"><svg width="10" height="13" viewBox="0 0 10 13" aria-hidden="true"><path d="M2 1.5l5 5-5 5" fill="none" stroke="#6b6b6b" stroke-width="2.6"/></svg>Praesent vestibulum molestie lacus. Aenean .</li>
      <li class="point"><svg width="10" height="13" viewBox="0 0 10 13" aria-hidden="true"><path d="M2 1.5l5 5-5 5" fill="none" stroke="#6b6b6b" stroke-width="2.6"/></svg>Praesent vestibulum molestie lacus. Aenean .</li>
      <li class="point"><svg width="10" height="13" viewBox="0 0 10 13" aria-hidden="true"><path d="M2 1.5l5 5-5 5" fill="none" stroke="#6b6b6b" stroke-width="2.6"/></svg>Praesent vestibulum molestie lacus. Aenean .</li>
    </ul>
  </main>

  <footer class="site-footer">© 2012 Veranto Solutions Limited.</footer>
</body>
</html>
```